Website for new child psychology practice

New clinical psychology practice in NSW Australia, specialising in work with children, adolescents and families. I would like to feature the colours in the logo, which was recently designed by pixelhive designer Odette.
I am seeking a professional looking page, which is easy to navigate and is colourful and playful but not childish.
Target Market(s)
Parents and professionals
Industry/Entity Type
Health
Coding
Coded - Design and coding required
Number of Pages Required
1 page
Font styles to use
Serif
Requirements
Must have
- Pages for 'About us' 'Services' 'Fees and information' 'Contact us'
Should not have
- Childish stock photos

```html
<!DOCTYPE html>
<html lang="en">
<head>
<meta charset="utf-8">
<title>Dr Helena Marsh – Clinical Psychology Practice</title>
<link rel="stylesheet" href="https://fonts.googleapis.com/css2?family=Cinzel:wght@400;500;600;700&family=Poppins:wght@400;500;600&display=swap">
<style>
:root{
  --purple:#9b2c8c;
  --purple-dark:#7a1f6c;
  --plum:#6e1a5e;
  --magenta:#b0369f;
  --orange:#e3642d;
  --orange-soft:#ec8a35;
  --yellow:#f8c46f;
  --pink-bg:#f7e8f3;
  --ink:#1c1c1c;
  --body:#3c3c3c;
  --white:#ffffff;
}
*{margin:0;padding:0;box-sizing:border-box}
html,body{width:1200px;height:4027px;overflow:hidden}
body{position:relative;background:var(--white);font-family:'Poppins',sans-serif;color:var(--body)}
.abs{position:absolute}
.serif{font-family:'Cinzel',serif}
.btn{position:absolute;display:flex;align-items:center;justify-content:center;border-radius:30px;font-family:'Cinzel',serif;font-size:14px;letter-spacing:1px;color:var(--white)}
.btn-orange{background:linear-gradient(90deg,var(--orange),var(--orange-soft))}
.btn-purple{background:linear-gradient(90deg,var(--purple-dark),var(--magenta))}
.photo{position:absolute;border-radius:50%}
.label{position:absolute;font-family:'Cinzel',serif;letter-spacing:3px;font-size:20px}
.heading{position:absolute;font-family:'Cinzel',serif;font-weight:500;letter-spacing:2px;color:var(--ink);white-space:nowrap}
.para{position:absolute;font-size:16px;line-height:27px;color:var(--body)}

/* top bar */
.top-rule{left:0;top:0;width:1200px;height:5px;background:linear-gradient(90deg,var(--orange),var(--purple),var(--orange-soft))}
.brand{position:absolute;display:flex;align-items:center;gap:10px}
.brand-dot{width:58px;height:58px;border-radius:50%;background:var(--purple)}
.brand-name{font-family:'Cinzel',serif;font-size:30px;color:var(--ink);line-height:1}
.brand-sub{font-family:'Cinzel',serif;font-size:11px;letter-spacing:3px;color:var(--ink);margin-top:3px}
.nav a{position:absolute;top:40px;font-family:'Cinzel',serif;font-size:14px;color:var(--ink);text-decoration:none;letter-spacing:.5px}
.nav .active::after{content:"";position:absolute;left:8px;right:8px;bottom:-10px;height:2px;background:var(--purple)}

/* hero */
.hero{left:0;top:5px;width:1200px;height:700px;background:linear-gradient(160deg,#f4e3f0,#f9eef6 60%,#f3dff0)}
.hero-title{position:absolute;left:122px;top:240px;font-family:'Cinzel',serif;font-weight:600;font-size:56px;line-height:50px;letter-spacing:3px}

/* services */
.card{position:absolute;top:1528px;width:285px;height:232px;border:2px solid rgba(248,196,111,.7);text-align:center}
.card-icon{position:absolute;left:50%;top:-46px;transform:translateX(-50%);width:96px;height:96px;border-radius:50% 50% 50% 8px}
.card h3{margin-top:66px;font-family:'Cinzel',serif;font-weight:500;font-size:20px;color:var(--white);letter-spacing:1px}
.card p{margin:12px 26px 0;font-size:11px;line-height:20px;color:rgba(255,255,255,.85)}
.card .pill{margin:18px auto 0;width:144px;height:36px;border:2px solid var(--yellow);border-radius:20px;font-family:'Cinzel',serif;font-size:12px;color:var(--white);display:flex;align-items:center;justify-content:center}

/* testimonials */
.tcard{position:absolute;top:2667px;width:310px;height:250px;border:1.5px solid #e2b9d6;background:var(--white);box-shadow:0 4px 14px rgba(155,44,140,.08)}
.tcard p{margin:36px 30px 0 34px;font-size:13px;line-height:22px;color:var(--body)}
.tcard .who{position:absolute;left:34px;top:190px;display:flex;align-items:center;gap:10px}
.avatar{width:36px;height:36px;border-radius:50%;background:linear-gradient(135deg,#d9b49a,#a7857a)}
.who b{display:block;font-size:12px;font-weight:600;color:var(--ink)}
.stars{color:var(--orange-soft);font-size:13px;letter-spacing:2px}
.review-mark{position:absolute;right:22px;top:204px;width:24px;height:24px;border-radius:50%;background:#d9d9d9}
.arrow{position:absolute;top:2772px}

/* contact */
.field{position:absolute;left:143px;width:412px;height:45px;background:var(--white);font-size:13px;color:#333;padding:14px 20px}

/* footer */
.footer-head{position:absolute;font-family:'Cinzel',serif;font-size:22px;color:var(--ink);letter-spacing:1px}
.footer-head::before{content:"";position:absolute;left:-36px;top:2px;width:3px;height:24px;background:var(--purple)}
.links{position:absolute;left:548px;top:3740px;font-size:14px;line-height:27px;color:var(--ink)}
.contact-row{position:absolute;left:782px;display:flex;gap:14px;font-size:14px;color:var(--ink);line-height:22px}
.c-icon{width:42px;height:42px;border-radius:50% 50% 50% 6px;background:var(--magenta);display:flex;align-items:center;justify-content:center}
.social{position:absolute;top:3805px;width:42px;height:42px;border-radius:50%;background:var(--purple)}
</style>
</head>
<body>

<!-- HERO -->
<div class="abs hero"></div>
<svg class="abs" style="left:0;top:500px" width="1200" height="220" viewBox="0 0 1200 220">
  <path d="M0 80 C 180 170, 420 190, 700 190 C 900 190, 1050 185, 1200 190 L1200 220 L0 220 Z" fill="#fff"/>
  <path d="M0 80 C 180 170, 420 185, 700 183 C 900 182, 1050 180, 1200 185 L1200 192 C 1050 188, 900 192, 700 200 C 420 205, 180 190, 0 110 Z" fill="url(#swoosh)"/>
  <defs><linearGradient id="swoosh" x1="0" x2="1"><stop offset="0" stop-color="#9b2c8c"/><stop offset=".7" stop-color="#9b2c8c"/><stop offset="1" stop-color="#9b2c8c" stop-opacity="0"/></linearGradient></defs>
</svg>
<div class="abs top-rule"></div>

<header>
  <div class="brand" style="left:100px;top:20px">
    <div class="brand-dot"></div>
    <div><div class="brand-name">Dr Helena Marsh</div><div class="brand-sub">Clinical Psychologist</div></div>
  </div>
  <nav class="nav">
    <a href="#about" class="active" style="left:476px">ABOUT US</a>
    <a href="#services" style="left:596px">SERVICES</a>
    <a href="#fees" style="left:709px">FEES &amp; INFORMATION</a>
  </nav>
  <div class="btn btn-purple" style="left:918px;top:28px;width:157px;height:44px">CONTACT US</div>
</header>

<div class="abs" style="left:0;top:226px;width:110px;height:2px;background:var(--purple)"></div>
<div class="abs serif" style="left:128px;top:212px;font-size:22px;letter-spacing:2px;color:var(--ink)">Dr Helena Marsh</div>
<h1 class="hero-title"><span style="color:var(--ink)">CLINICAL</span><br><span style="color:var(--purple)">PSYCHOLOGY</span><br><span style="color:var(--orange)">PRACTICE</span></h1>
<div class="btn btn-orange" style="left:122px;top:422px;width:270px;height:50px;justify-content:flex-start;padding-left:30px">SCHEDULE APPOINTMENT</div>
<div class="abs" style="left:352px;top:418px;width:56px;height:56px;border-radius:50% 50% 50% 6px;background:var(--purple);border:4px solid #fff"></div>

<div class="abs" style="left:603px;top:414px;width:186px;height:152px;border-radius:50% 14px 50% 50%;background:var(--yellow)"></div>
<div class="abs" style="left:867px;top:414px;width:133px;height:106px;border-radius:14px 50% 50% 50%;background:var(--orange)"></div>
<div class="photo" role="img" aria-label="Photo of a father and teenage son talking on a sofa" style="left:612px;top:208px;width:200px;height:212px;background:linear-gradient(135deg,#c9b6a8,#5a5f70)"></div>
<div class="abs" role="img" aria-label="Illustration of a tree growing inside a head over a purple landscape" style="left:820px;top:97px;width:296px;height:336px;border-radius:50% 50% 50% 12px;background:radial-gradient(circle at 50% 45%,#e7a4d9,#b03c9f 60%,#8a2079)"></div>
<div class="photo" role="img" aria-label="Photo of a thoughtful teenage boy with hands clasped" style="left:766px;top:469px;width:152px;height:172px;background:linear-gradient(135deg,#c8ccd6,#3e5a86)"></div>

<!-- ABOUT -->
<div class="abs" role="img" aria-label="Faint decorative contour pattern" style="left:0;top:700px;width:320px;height:420px;background:radial-gradient(ellipse at 0% 50%,rgba(225,225,225,.45),rgba(255,255,255,0) 70%)"></div>
<div class="abs" style="left:95px;top:755px;width:470px;height:470px;border-radius:50%;background:var(--yellow)"></div>
<div class="abs" style="left:118px;top:770px;width:450px;height:450px;border-radius:50%;background:var(--purple)"></div>
<div class="photo" role="img" aria-label="Portrait photo of the psychologist holding a notepad" style="left:124px;top:778px;width:432px;height:432px;background:linear-gradient(135deg,#d8c7b6,#9a8e86)"></div>

<section id="about">
  <div class="label" style="left:610px;top:817px;color:var(--purple)">ABOUT US</div>
  <h2 class="heading" style="left:610px;top:847px;font-size:43px">Dr Helena Marsh</h2>
  <div class="abs" style="left:1088px;top:866px;width:112px;height:2px;background:var(--purple)"></div>
  <div class="abs" style="left:1088px;top:862px;width:9px;height:9px;border-radius:50%;background:var(--purple)"></div>
  <p class="para" style="left:615px;top:910px;width:460px">Lorem ipsum dolor sit amet, consectetur adipiscing elit, sed do eiusmod tempor incididunt ut labore et dolore magna aliqua. Quis ipsum suspendisse ultrices gravida. Risus commodo viverra maecenas accumsa</p>
  <p class="para" style="left:615px;top:1045px;width:460px">Lorem ipsum dolor sit amet, consectetur adipiscing elit, sed do eiusmod tempor incididunt ut labore et dolore</p>
  <div class="btn btn-orange" style="left:607px;top:1126px;width:192px;height:47px">LEARN MORE</div>
</section>

<!-- SERVICES -->
<svg class="abs" style="left:0;top:1290px" width="1200" height="625" viewBox="0 0 1200 625" aria-hidden="true">
  <defs><linearGradient id="svc" x1="0" x2="1"><stop offset="0" stop-color="#7a1f6c"/><stop offset="1" stop-color="#a9329a"/></linearGradient></defs>
  <path d="M0 14 C 300 0, 700 0, 1200 95 L1200 70 C 900 -10, 600 -5, 0 8 Z" fill="var(--orange-soft)"/>
  <path d="M0 14 C 300 2, 700 8, 1200 95 L1200 600 C 900 640, 500 650, 0 520 Z" fill="url(#svc)"/>
  <path d="M0 505 C 300 600, 700 620, 1200 585 L1200 600 C 800 630, 400 630, 0 545 Z" fill="var(--yellow)"/>
</svg>
<section id="services">
  <div class="label" style="left:0;width:1200px;text-align:center;top:1370px;color:var(--yellow)">WHAT WE DO</div>
  <h2 class="heading" style="left:0;width:1200px;text-align:center;top:1390px;font-size:42px;color:var(--white)">Services Provide</h2>
  <div class="abs" style="left:553px;top:1446px;width:94px;height:2px;background:var(--yellow)"></div>
  <div class="abs" style="left:596px;top:1443px;width:8px;height:8px;border-radius:50%;background:var(--orange-soft)"></div>

  <div class="card" style="left:147px"><div class="card-icon" role="img" aria-label="Service icon: head with brain" style="background:radial-gradient(circle at 50% 45%,#e69ad8,#c35cb2)"></div><h3>Services Heading</h3><p>Lorem ipsum dolor sit amet, consectetur adipiscing elit, sed do eiusmod teLorem ipsum dolor sit</p><div class="pill">LEARN MORE</div></div>
  <div class="card" style="left:451px"><div class="card-icon" role="img" aria-label="Service icon: head with connected ideas" style="background:radial-gradient(circle at 50% 45%,#f5935a,var(--orange))"></div><h3>Services Heading</h3><p>Lorem ipsum dolor sit amet, consectetur adipiscing elit, sed do eiusmod teLorem ipsum dolor sit</p><div class="pill">LEARN MORE</div></div>
  <div class="card" style="left:753px"><div class="card-icon" role="img" aria-label="Service icon: head with puzzle thoughts" style="background:radial-gradient(circle at 50% 45%,#fbd898,var(--yellow))"></div><h3>Services Heading</h3><p>Lorem ipsum dolor sit amet, consectetur adipiscing elit, sed do eiusmod teLorem ipsum dolor sit</p><div class="pill">LEARN MORE</div></div>
</section>

<!-- FEES -->
<div class="abs" style="left:0;top:1905px;width:1200px;height:590px;background:linear-gradient(90deg,#f5e2ee,#fbf3f8)"></div>
<div class="abs" role="img" aria-label="Photo of a smiling psychologist with a clipboard in session with a young girl" style="left:500px;top:1900px;width:700px;height:595px;background:linear-gradient(90deg,rgba(245,226,238,0),#e5dcd6 18%,#d6cdc7 60%,#c8bdb4)"></div>
<section id="fees">
  <div class="label" style="left:145px;top:1998px;color:var(--purple)">FEE &amp; INFORMATION</div>
  <h2 class="heading" style="left:143px;top:2025px;font-size:46px">Our Fees</h2>
  <div class="abs" style="left:148px;top:2087px;width:80px;height:2px;background:#c9a3bf"></div>
  <div class="abs" style="left:146px;top:2084px;width:8px;height:8px;border-radius:50%;background:var(--purple)"></div>
  <p class="para" style="left:146px;top:2113px;width:365px;font-size:14px;line-height:23px">Lorem ipsum dolor sit amet, consectetur adipiscing elit, sed do eiusmod tempor incididunt ut labore</p>
  <p class="para" style="left:146px;top:2183px;width:365px;font-size:14px;line-height:23px;text-align:justify">At dolore magna aliqua. Quis ipsum suspendisse ultrices Lorem ipsum dolor sit amet, consectetur adipiscing elit, sed do eiusmod tempor incididunt ut labore et dolore ultrices Lorem ipsum dolor sit</p>
  <div class="btn btn-purple" style="left:147px;top:2297px;width:178px;height:46px">LEARN MORE</div>
</section>

<!-- TESTIMONIALS -->
<section>
  <div class="label" style="left:0;width:1210px;text-align:center;top:2558px;font-size:17px;color:var(--purple)">PEOPLE WORDS</div>
  <h2 class="heading" style="left:0;width:1210px;text-align:center;top:2578px;font-size:40px">Testimonials</h2>
  <svg class="arrow" style="left:74px" width="22" height="36" viewBox="0 0 22 36"><path d="M18 3 L4 18 L18 33" fill="none" stroke="var(--purple)" stroke-width="3"/></svg>
  <svg class="arrow" style="left:1130px" width="22" height="36" viewBox="0 0 22 36"><path d="M4 3 L18 18 L4 33" fill="none" stroke="var(--purple)" stroke-width="3"/></svg>

  <div class="tcard" style="left:124px"><p>Lorem ipsum dolor sit amet, consectetur adipiscing elit, sed do eiusmod tempor incididunt ut labore et dolore magna aliqua. Quis ipsum suspendisse ultrices gravida. Risus commodo viverra maecenas acc</p><div class="who"><div class="avatar"></div><div><b>Daniel Price</b><span class="stars">★★★★★</span></div></div><div class="review-mark"></div></div>
  <div class="tcard" style="left:457px"><p>Lorem ipsum dolor sit amet, consectetur adipiscing elit, sed do eiusmod tempor incididunt ut labore et dolore magna aliqua. Quis ipsum suspendisse ultrices gravida. Risus commodo viverra maecenas acc</p><div class="who"><div class="avatar"></div><div><b>Daniel Price</b><span class="stars">★★★★★</span></div></div><div class="review-mark"></div></div>
  <div class="tcard" style="left:788px"><p>Lorem ipsum dolor sit amet, consectetur adipiscing elit, sed do eiusmod tempor incididunt ut labore et dolore magna aliqua. Quis ipsum suspendisse ultrices gravida. Risus commodo viverra maecenas acc</p><div class="who"><div class="avatar"></div><div><b>Daniel Price</b><span class="stars">★★★★★</span></div></div><div class="review-mark"></div></div>
</section>

<!-- CONTACT -->
<svg class="abs" style="left:0;top:2995px" width="1200" height="640" viewBox="0 0 1200 640" aria-hidden="true">
  <defs><linearGradient id="ct" x1="0" x2="1"><stop offset="0" stop-color="#7a1f6c"/><stop offset=".5" stop-color="#a9379b"/><stop offset="1" stop-color="#d184c4"/></linearGradient></defs>
  <path d="M0 10 C 400 -5, 800 0, 1200 100 L1200 75 C 800 -15, 400 -15, 0 4 Z" fill="var(--orange-soft)"/>
  <path d="M0 10 C 400 0, 800 10, 1200 100 L1200 600 C 800 640, 400 630, 0 520 Z" fill="url(#ct)"/>
  <path d="M0 505 C 350 600, 750 620, 1200 590 L1200 605 C 750 640, 350 630, 0 540 Z" fill="var(--yellow)"/>
</svg>
<section id="contact">
  <div class="abs" style="left:0;top:3125px;width:108px;height:2px;background:var(--yellow)"></div>
  <div class="label" style="left:143px;top:3083px;font-size:18px;color:var(--yellow)">GET IN TOUCH</div>
  <h2 class="heading" style="left:143px;top:3103px;font-size:38px;color:var(--white)">Contact Us</h2>
  <div class="field" style="top:3171px">Name*</div>
  <div class="field" style="top:3225px">Email address*</div>
  <div class="field" style="top:3279px">Subject*</div>
  <div class="field" style="top:3334px;height:91px">Message</div>
  <div class="btn" style="left:143px;top:3443px;width:187px;height:45px;background:var(--plum);font-family:'Poppins',sans-serif;font-weight:600;font-size:13px;letter-spacing:0">SEND MESSAGE</div>
  <div class="abs" style="left:617px;top:3070px;width:470px;height:470px;border-radius:50%;background:var(--yellow)"></div>
  <div class="abs" style="left:630px;top:3090px;width:458px;height:458px;border-radius:50%;background:var(--purple)"></div>
  <div class="photo" role="img" aria-label="Photo of smiling parents and daughter at a table" style="left:640px;top:3097px;width:436px;height:436px;background:linear-gradient(135deg,#e9ddd0,#b7b2bf 60%,#8aa0c4)"></div>
</section>

<!-- FOOTER -->
<footer>
  <div class="abs" style="left:508px;top:3640px;width:1px;height:315px;background:#e0e0e0"></div>
  <div class="abs" style="left:755px;top:3640px;width:1px;height:315px;background:#e0e0e0"></div>
  <div class="abs" style="left:272px;top:3680px;width:50px;height:50px;border-radius:50%;background:var(--purple)"></div>
  <div class="abs serif" style="left:140px;top:3737px;width:315px;text-align:center;font-size:30px;color:var(--ink)">Dr Helena Marsh</div>
  <div class="abs serif" style="left:140px;top:3773px;width:315px;text-align:center;font-size:11px;letter-spacing:3px;color:var(--ink)">Clinical Psychologist</div>
  <div class="social" style="left:224px"></div>
  <div class="social" style="left:274px;background:#c084b6"></div>
  <div class="social" style="left:324px;background:#c06bb3"></div>

  <div class="footer-head" style="left:545px;top:3700px">Quick Links</div>
  <div class="links">Home<br>About Us<br>Services<br>Fees &amp; Information<br>Contact Us</div>

  <div class="footer-head" style="left:785px;top:3700px">Contact Us</div>
  <div class="contact-row" style="top:3745px">
    <div class="c-icon"><svg width="20" height="20" viewBox="0 0 24 24"><path d="M6.6 10.8a15 15 0 0 0 6.6 6.6l2.2-2.2a1 1 0 0 1 1-.25 11.4 11.4 0 0 0 3.6.57 1 1 0 0 1 1 1V20a1 1 0 0 1-1 1A17 17 0 0 1 3 4a1 1 0 0 1 1-1h3.5a1 1 0 0 1 1 1c0 1.250.2 2.45.57 3.57a1 1 0 0 1-.25 1z" fill="#fff"/></svg></div>
    <div>Phone Number<br><b style="font-weight:500">(555) 014-2290</b></div>
  </div>
  <div class="contact-row" style="top:3815px">
    <div class="c-icon"><svg width="20" height="20" viewBox="0 0 24 24"><path d="M3 5h18v14H3z" fill="#fff"/><path d="M3 5l9 7 9-7" fill="none" stroke="#b0369f" stroke-width="2"/></svg></div>
    <div>Email address<br>hello@marshpractice.com</div>
  </div>

  <div class="abs" style="left:0;top:3955px;width:1200px;height:1px;background:#e0e0e0"></div>
  <div class="abs" style="left:0;top:3982px;width:1200px;text-align:center;font-size:12px;color:#555">© 2024 Dr Helena Marsh. All Rights Reserved</div>
</footer>

</body>
</html>
```